I would like a simple but elegant desing that is eye catching. I design floral arrangements for all types of parties, and sew mariachi trajes (outfits). I would like somehow to combine floral and mariachi together or a design that indicates Fiesta/party. Disregard color any color will be fine to match simplicity of design.

Target Market(s)

Adults and teenagers

Industry/Entity Type

Floral

Contact Information for Business Card

"Marigold Lane"
Specializing on floral designs for all ocassions
Contact Marla Quintero
(210) 637-1185
We have the connections to meet all your party needs..
E-mail: bellomontesgraciela@mailvista.example

Font styles to use
Decorative
Script

Colors

Designer to choose colors to be used in the design.

Requirements
Must have
• Simple, eye catching
Nice to have
• Logo could have a mariachi hat with light floral background or could be simply an abstract design

```html
<!DOCTYPE html>
<html lang="en">
<head>
<meta charset="utf-8">
<title>Marigold Lane – Business Card</title>
<link rel="stylesheet" href="https://fonts.googleapis.com/css2?family=Great+Vibes&family=Crimson+Text:ital,wght@0,400;1,400&display=swap">
<style>
  :root {
    --page: #d9d9d9;
    --card: #050505;
    --ink: #f4f1ea;
    --gold: #e2b82b;
    --vine: #4a4536;
    --vine-soft: #2a271f;
    --hat-blue: #2f7fd0;
    --hat-gold: #c9962e;
  }
  * { margin: 0; padding: 0; box-sizing: border-box; }
  html, body { width: 1200px; height: 900px; overflow: hidden; background: var(--page); }
  .stage {
    width: 1200px; height: 900px;
    display: flex; flex-direction: column; align-items: center; justify-content: center; gap: 24px;
  }
  .card {
    position: relative; width: 700px; height: 400px;
    background: var(--card); overflow: hidden;
    box-shadow: 0 6px 18px rgba(0,0,0,.25);
  }
  .vine {
    position: absolute; width: 220px; height: 300px;
    background: radial-gradient(ellipse at center, var(--vine) 0%, var(--vine-soft) 55%, transparent 75%);
    opacity: .55;
  }
  .vine--left { left: -30px; top: 80px; }
  .vine--right { right: -30px; top: 30px; }
  .sombrero {
    position: absolute; width: 140px; height: 72px; border-radius: 50%;
    background: radial-gradient(ellipse at 50% 40%, var(--hat-blue) 0%, var(--hat-blue) 35%, var(--hat-gold) 70%, #8a6520 100%);
  }
  .sombrero--top { left: 36px; top: 20px; }
  .sombrero--bottom { right: 36px; bottom: 22px; }
  .brand {
    position: absolute; left: 0; right: 0; top: 130px; text-align: center; color: var(--ink);
  }
  .brand__name {
    font-family: "Great Vibes", cursive; font-size: 72px; line-height: 1; font-weight: 400;
  }
  .rule { width: 380px; height: 2px; background: var(--gold); margin: 8px auto 10px; }
  .brand__tagline {
    font-family: "Great Vibes", cursive; font-size: 26px; line-height: 1.2;
  }
  .contact {
    position: absolute; left: 0; right: 0; top: 88px; text-align: center; color: var(--ink);
    font-family: "Crimson Text", serif;
  }
  .contact__name { font-family: "Great Vibes", cursive; font-size: 60px; line-height: 1; font-weight: 400; }
  .contact__rule { width: 300px; }
  .contact__phone { display: flex; align-items: center; justify-content: center; gap: 12px; font-size: 22px; margin-top: 4px; }
  .phone-icon { width: 22px; height: 22px; background: var(--gold); border-radius: 3px; display: flex; align-items: center; justify-content: center; }
  .contact__email { font-size: 20px; margin-top: 6px; }
  .contact__tagline { font-size: 18px; font-style: italic; margin-top: 8px; }
</style>
</head>
<body>
<main class="stage">
  <section class="card card--front">
    <div class="vine vine--left" role="img" aria-label="Faint olive floral vine ornament"></div>
    <div class="vine vine--right" role="img" aria-label="Faint olive floral vine ornament"></div>
    <div class="sombrero sombrero--top" role="img" aria-label="Blue and gold embroidered mariachi sombrero illustration"></div>
    <div class="brand">
      <h1 class="brand__name">Marigold Lane</h1>
      <div class="rule"></div>
      <p class="brand__tagline">Floral artistry crafted for every celebration</p>
    </div>
    <div class="sombrero sombrero--bottom" role="img" aria-label="Blue and gold embroidered mariachi sombrero illustration"></div>
  </section>

  <section class="card card--contact">
    <div class="vine vine--left" role="img" aria-label="Faint olive floral vine ornament"></div>
    <div class="vine vine--right" role="img" aria-label="Faint olive floral vine ornament"></div>
    <div class="sombrero sombrero--top" role="img" aria-label="Blue and gold embroidered mariachi sombrero illustration"></div>
    <div class="contact">
      <h2 class="contact__name">Marla Quintero</h2>
      <div class="rule contact__rule"></div>
      <p class="contact__phone">
        <span class="phone-icon">
          <svg width="14" height="14" viewBox="0 0 24 24" aria-hidden="true"><path fill="#050505" d="M6.6 10.8a15 15 0 0 0 6.6 6.6l2.2-2.2a1 1 0 0 1 1-.25 11.4 11.4 0 0 0 3.6.57 1 1 0 0 1 1 1V20a1 1 0 0 1-1 1A17 17 0 0 1 3 4a1 1 0 0 1 1-1h3.5a1 1 0 0 1 1 1c0 1.25.2 2.45.57 3.6a1 1 0 0 1-.25 1z"/></svg>
        </span>
        (210) 637-1185
      </p>
      <p class="contact__email">bellomontesgraciela@mailvista.example</p>
      <p class="contact__tagline">Every detail for your celebration, all in one place</p>
    </div>
    <div class="sombrero sombrero--bottom" role="img" aria-label="Blue and gold embroidered mariachi sombrero illustration"></div>
  </section>
</main>
</body>
</html>
```